Tallow Crest Business Card

We need a business card designed for a a company called "Tallow Crest". We offer consulting, coaching and training to business leaders and coaches (across the world) using the latest findings in neuroscience, social and emotional intelligence and positive psychology. The final design should communicate the use of brain science to create sustainable relationships.

The card should be doublesided. The logo is attached and names and titles will be provided to the successful designer. Thank you.

Industry/Entity Type

Training

```html
<!DOCTYPE html>
<html lang="en">
<head>
<meta charset="utf-8">
<title>Tallow Crest Business Card</title>
<link href="https://fonts.googleapis.com/css2?family=Open+Sans:wght@400;700&display=swap" rel="stylesheet">
<style>
  :root {
    --teal: #007c9a;
    --teal-dark: #0a6f8a;
    --lime: #b5dc10;
    --mist: #c4e0e8;
    --paper: #ffffff;
    --ink-soft: #6b6f73;
    --stage: #d9dcdf;
  }
  * { margin: 0; padding: 0; box-sizing: border-box; }
  html, body {
    width: 1200px; height: 900px; overflow: hidden;
    background: var(--stage);
    font-family: "Open Sans", Arial, sans-serif;
  }
  .card {
    position: absolute;
    left: 280px;
    width: 640px; height: 366px;
    border-radius: 18px;
    overflow: hidden;
    box-shadow: 0 6px 18px rgba(0,0,0,.18);
  }
  /* back side */
  .card-back { top: 56px; background: var(--teal); }
  .card-back .brand-mark {
    position: absolute; left: 70px; top: 70px;
    width: 150px; height: 150px; border-radius: 50%;
    background: var(--lime);
  }
  .card-back .brand-name {
    position: absolute; right: 44px; bottom: 54px;
    font-weight: 700; font-size: 62px; letter-spacing: 1px;
    color: var(--paper);
  }
  /* front side */
  .card-front { top: 478px; background: var(--paper); }
  .card-front .accent-shape {
    position: absolute; right: -70px; top: 70px;
    width: 300px; height: 300px; border-radius: 50%;
    background: var(--mist);
  }
  .person { position: absolute; right: 40px; top: 26px; text-align: right; }
  .person-name { color: var(--teal); font-weight: 700; font-size: 22px; line-height: 1.1; }
  .person-role { color: var(--ink-soft); font-size: 14px; }
  .brand-lockup {
    position: absolute; left: 40px; top: 118px;
    display: flex; align-items: center; gap: 10px;
  }
  .brand-lockup .brand-mark {
    width: 26px; height: 26px; background: var(--lime);
  }
  .brand-lockup .brand-name {
    color: var(--teal); font-weight: 700; font-size: 34px;
  }
  .contact {
    position: absolute; left: 40px; top: 214px;
    color: var(--ink-soft); font-size: 16px; line-height: 1.5;
  }
  .contact-address { margin-bottom: 14px; }
  .contact-grid { display: grid; grid-template-columns: 200px auto; row-gap: 4px; }
  .contact-item { display: flex; align-items: center; gap: 8px; }
  .contact-item svg { width: 16px; height: 16px; flex: none; }
</style>
</head>
<body>

<section class="card card-back" aria-label="Card back">
  <div class="brand-mark"></div>
  <div class="brand-name">Tallow Crest</div>
</section>

<section class="card card-front" aria-label="Card front">
  <div class="accent-shape"></div>

  <div class="person">
    <div class="person-name">Lena Hartwell</div>
    <div class="person-role">Marketing Manager</div>
  </div>

  <div class="brand-lockup">
    <div class="brand-mark"></div>
    <div class="brand-name">Tallow Crest</div>
  </div>

  <div class="contact">
    <div class="contact-address">PO Box 118 Ridgewater SA 5091</div>
    <div class="contact-grid">
      <div class="contact-item">
        <svg viewBox="0 0 16 16" aria-hidden="true"><path d="M2 6c0-2 3-3 6-3s6 1 6 3l-2 1-1-2H5L4 7z M4 8h8l1 5H3z" fill="var(--teal-dark)"/></svg>
        (08) 5550 3184
      </div>
      <div class="contact-item">
        <svg viewBox="0 0 16 16" aria-hidden="true"><rect x="1.5" y="3.5" width="13" height="9" fill="none" stroke="var(--teal-dark)" stroke-width="1.3"/><path d="M1.5 3.5 8 9l6.5-5.5" fill="none" stroke="var(--teal-dark)" stroke-width="1.3"/></svg>
        lena@tallowcrest.com
      </div>
      <div class="contact-item">
        <svg viewBox="0 0 16 16" aria-hidden="true"><rect x="4" y="1.5" width="8" height="5" fill="none" stroke="var(--teal-dark)" stroke-width="1.3"/><rect x="1.5" y="6.5" width="13" height="6" rx="1" fill="var(--teal-dark)"/><rect x="4" y="10" width="8" height="4.5" fill="var(--paper)" stroke="var(--teal-dark)" stroke-width="1.2"/></svg>
        0400 555 219
      </div>
      <div class="contact-item">
        <svg viewBox="0 0 16 16" aria-hidden="true"><circle cx="8" cy="8" r="6.5" fill="none" stroke="var(--teal-dark)" stroke-width="1.3"/><ellipse cx="8" cy="8" rx="3" ry="6.5" fill="none" stroke="var(--teal-dark)" stroke-width="1.1"/><path d="M1.5 8h13M2.8 4.5h10.4M2.8 11.5h10.4" stroke="var(--teal-dark)" stroke-width="1.1"/></svg>
        www.tallowcrest.com
      </div>
    </div>
  </div>
</section>

</body>
</html>
```